Business Cards for Marco and Tobin

Design of business cards for two people with the recently created brand Valcor Mobile. Valcor Mobile wants to become a worldwide major player on the secondhand phone market. It gathers send hand phones from individuals, refurbish them and sell them throughout the world. It has a green impact (recycling) and we also contribute to social project in Africa (a percentage of our benefits are sent to build school, sport facilities, etc.

Target Market(s)

B2B - Marco and Tobin are in contact with distributors across Africa.

Industry/Entity Type

Wireless Communication

Contact Information for Business Card

Marco Feuillet
Head of Emerging Markets
Valcor Energy South Africa (Pty) Ltd
Kestrel Road 47
2031 Sandton - Johannesburg
South Africa
Tel: + 27 10 555 0148
Mobile : +27 82 55 104
Email : marco.feuillet@valcormobile.example
Skype: marco.feuillet
Web: www.valcormobile.example
 

Tobin Farrow
Head of Southern Africa
Kestrel Road 47
South Africa
Tel: + 27 10 555 0148
Mobile: +27 83 555 0276
Email: tobin.farrow@valcormobile.example
Skype: tobin.farrow
Web: www.valcormobile.example

Requirements
Must have
• The cards need to be "serious", trustable, with a worldwide presence.
Nice to have
• Some "green" / recycling touch would be nice but not necessary if in contradiction with the general design.

```html
<!DOCTYPE html>
<html lang="en">
<head>
<meta charset="utf-8">
<title>Valcor Mobile – Business Cards</title>
<link rel="stylesheet" href="https://fonts.googleapis.com/css2?family=Arimo:wght@400;700&display=swap">
<style>
  :root {
    --bg: #e8e9eb;
    --brand-blue: #2a95d4;
    --brand-blue-dark: #1f82c2;
    --navy: #1d3553;
    --text-grey: #5f6670;
    --rule: #cfd3d8;
    --card-white: #ffffff;
  }
  * { box-sizing: border-box; margin: 0; padding: 0; }
  html, body { width: 1200px; height: 800px; overflow: hidden; }
  body {
    background: var(--bg);
    font-family: "Arimo", Arial, sans-serif;
    position: relative;
  }
  .card {
    position: absolute;
    width: 540px;
    height: 310px;
    border-radius: 24px;
    overflow: hidden;
    box-shadow: 0 10px 24px rgba(0,0,0,0.12);
  }

  /* Back of card */
  .card-back {
    left: 70px; top: 110px;
    background: linear-gradient(160deg, #3aa3de 0%, var(--brand-blue) 55%, var(--brand-blue-dark) 100%);
    display: flex; align-items: center; justify-content: center; gap: 12px;
  }
  .card-back .brand-square {
    width: 22px; height: 22px; background: #ffffff; border-radius: 3px;
  }
  .card-back .brand-name {
    color: #ffffff; font-weight: 700; font-size: 30px; letter-spacing: -0.3px;
  }

  /* Front of card */
  .card-front {
    left: 590px; top: 380px;
    background: var(--card-white);
  }
  .top-stripe {
    position: absolute; right: 0; top: 14px;
    width: 250px; height: 8px; background: var(--brand-blue);
  }
  .name-tab {
    position: absolute; right: 0; top: 22px;
    width: 230px; height: 30px;
    background: var(--brand-blue);
    border-radius: 15px 0 0 15px;
    color: #fff; font-weight: 700; font-size: 18px;
    display: flex; align-items: center; padding-left: 18px;
  }
  .job-title {
    position: absolute; left: 312px; top: 60px;
    font-size: 12px; color: var(--navy);
  }
  .chat-handle {
    position: absolute; left: 312px; top: 80px;
    font-size: 12px; color: var(--text-grey);
    display: flex; align-items: center; gap: 6px;
  }
  .chat-dot {
    width: 11px; height: 11px; border-radius: 50%; background: var(--brand-blue);
  }
  .header-rule {
    position: absolute; left: 300px; right: 28px; top: 106px;
    height: 1px; background: var(--rule);
  }
  .brand-lockup {
    position: absolute; left: 40px; top: 112px;
    display: flex; align-items: center; gap: 10px;
  }
  .brand-lockup .brand-square {
    width: 18px; height: 18px; background: var(--brand-blue); border-radius: 2px;
  }
  .brand-lockup .brand-name {
    font-weight: 700; font-size: 28px; color: var(--navy); letter-spacing: -0.3px;
  }
  .company-name {
    position: absolute; left: 40px; top: 160px;
    font-size: 17px; color: var(--navy);
  }
  .company-address {
    position: absolute; left: 40px; top: 184px;
    font-size: 11.5px; color: var(--text-grey);
  }
  .contact-block {
    position: absolute; top: 214px;
    display: flex; align-items: center; gap: 8px;
    font-size: 12px; color: var(--text-grey); line-height: 1.25;
  }
  .contact-phone { left: 40px; }
  .contact-web { left: 200px; }
  .contact-icon { width: 16px; height: 16px; flex: none; }
</style>
</head>
<body>

  <section class="card card-back" aria-label="Card back">
    <span class="brand-square"></span>
    <span class="brand-name">Valcor Mobile</span>
  </section>

  <section class="card card-front" aria-label="Card front">
    <div class="top-stripe"></div>
    <div class="name-tab">Marco Feuillet</div>
    <p class="job-title">Head of Emerging Markets</p>
    <p class="chat-handle"><span class="chat-dot"></span>marco.feuillet</p>
    <div class="header-rule"></div>

    <div class="brand-lockup">
      <span class="brand-square"></span>
      <span class="brand-name">Valcor Mobile</span>
    </div>

    <p class="company-name">Valcor Energy South Africa (Pty) Ltd</p>
    <p class="company-address">Kestrel Road 47, 2031 Sandton - Johannesburg, South Africa</p>

    <div class="contact-block contact-phone">
      <svg class="contact-icon" viewBox="0 0 24 24" aria-hidden="true">
        <path fill="#1d3553" d="M6.6 10.8a15.1 15.1 0 0 0 6.6 6.6l2.2-2.2a1 1 0 0 1 1-.25 11.4 11.4 0 0 0 3.6.57 1 1 0 0 1 1 1V20a1 1 0 0 1-1 1A17 17 0 0 1 3 4a1 1 0 0 1 1-1h3.5a1 1 0 0 1 1 1c0 1.25.2 2.45.57 3.57a1 1 0 0 1-.25 1z"/>
      </svg>
      <div>+27 10 555 0148<br>+27 82 55 104</div>
    </div>

    <div class="contact-block contact-web">
      <svg class="contact-icon" viewBox="0 0 24 24" aria-hidden="true">
        <circle cx="12" cy="12" r="10" fill="#1d3553"/>
        <g fill="none" stroke="#ffffff" stroke-width="1.3">
          <ellipse cx="12" cy="12" rx="4" ry="9.5"/>
          <line x1="2.5" y1="12" x2="21.5" y2="12"/>
          <line x1="4" y1="7.5" x2="20" y2="7.5"/>
          <line x1="4" y1="16.5" x2="20" y2="16.5"/>
        </g>
      </svg>
      <div>marco.feuillet@valcormobile.example<br>www.valcormobile.example</div>
    </div>
  </section>

</body>
</html>
```